Brickline Kit - iPhone app for tradespeople - UI design

Brickline Kit is an iPhone app for tradespeople (builders, carpenters, electricians, etc) which provides a range of tools that will assist with typical tasks, such as the calculation of unit conversion and spatial/volumetric/electrical measurements. The application also makes use of instruments available in the smartphone device to provide useful tools such as a spirit level, compass and torch.

The product is a simple menu-based application consisting of a number of menu and function screens. Each menu item will navigate the user to the function screen applicable to that menu item. Each function screen will contain the necessary inputs and features for perform its stated function.

The user interface should be designed with the tradesperson user in mind and as such should be simple, intuitive and durable with respect to its usability, interface design and branding elements.

Target Market(s)

Tradespeople (builders, carpenters, electricians, etc)

Industry/Entity Type

Trade

Font styles to use
Sans Serif

Requirements
Must have
• Refer to attached wireframes document...
• - Simple design
• - Consistent layout and theme
• - Screens and icons
Should not have
• - Tacky 3D images and textured backgrounds

```html
<!DOCTYPE html>
<html lang="en">
<head>
<meta charset="utf-8">
<title>Brickline Kit – Home Menu</title>
<link href="https://fonts.googleapis.com/css2?family=Open+Sans:wght@400;600&display=swap" rel="stylesheet">
<style>
  :root {
    --canvas-bg: #f3f4f6;
    --screen-bg: #262728;
    --status-bg: #f7f7f7;
    --status-text: #111111;
    --photo-dark: #1f2021;
    --photo-mid: #3a3b3d;
    --accent-blue: #0f80ff;
    --text-light: #ffffff;
  }
  * { box-sizing: border-box; margin: 0; padding: 0; }
  html, body {
    width: 1200px;
    height: 1000px;
    overflow: hidden;
    background: var(--canvas-bg);
    font-family: "Open Sans", sans-serif;
  }
  .app-screen {
    position: absolute;
    left: 341px;
    top: 41px;
    width: 518px;
    height: 917px;
    background: var(--screen-bg);
    overflow: hidden;
  }
  .hero-photo {
    position: absolute;
    inset: 0;
    background:
      radial-gradient(ellipse 55% 40% at 62% 28%, var(--photo-mid) 0%, transparent 70%),
      radial-gradient(ellipse 60% 45% at 55% 70%, #343537 0%, transparent 75%),
      linear-gradient(180deg, #2c2d2f 0%, var(--photo-dark) 100%);
  }
  .status-bar {
    position: absolute;
    top: 0; left: 0;
    width: 100%;
    height: 32px;
    background: var(--status-bg);
    color: var(--status-text);
    font-size: 17px;
    display: flex;
    align-items: center;
    padding: 0 10px;
  }
  .status-left { display: flex; align-items: center; gap: 6px; flex: 1; }
  .signal-dots { display: flex; gap: 2px; }
  .signal-dots span {
    width: 8px; height: 8px; border-radius: 50%;
    border: 1px solid var(--status-text);
  }
  .signal-dots span.on { background: var(--status-text); }
  .status-time { flex: 1; text-align: center; }
  .status-right { flex: 1; display: flex; justify-content: flex-end; align-items: center; gap: 6px; }
  .battery {
    width: 36px; height: 15px;
    border: 1.5px solid var(--status-text);
    border-radius: 3px;
    padding: 1.5px;
    position: relative;
  }
  .battery::after {
    content: ""; position: absolute; right: -4px; top: 4px;
    width: 2px; height: 5px; background: var(--status-text);
  }
  .battery i { display: block; width: 100%; height: 100%; background: var(--status-text); border-radius: 1px; }
  .brand {
    position: absolute;
    top: 134px; left: 0;
    width: 100%;
    text-align: center;
    color: var(--text-light);
  }
  .brand-mark {
    width: 80px; height: 80px;
    margin: 0 auto 28px;
    background: var(--text-light);
    border-radius: 6px;
  }
  .brand-name {
    font-size: 45px;
    font-weight: 400;
    letter-spacing: 1px;
    line-height: 1;
  }
  .menu {
    position: absolute;
    top: 346px; left: 34px;
    width: 450px;
    list-style: none;
  }
  .menu-item {
    height: 84px;
    margin-bottom: 8px;
    background: var(--accent-blue);
    color: var(--text-light);
    display: flex;
    align-items: center;
    justify-content: center;
    font-size: 19px;
    font-weight: 600;
    letter-spacing: 1.2px;
  }
  .contact-link {
    position: absolute;
    top: 826px; left: 0;
    width: 100%;
    text-align: center;
    color: var(--text-light);
    font-size: 19px;
    font-weight: 600;
    letter-spacing: 1.2px;
    text-decoration: underline;
    text-underline-offset: 4px;
  }
</style>
</head>
<body>
  <main class="app-screen">
    <div class="hero-photo" role="img" aria-label="Dimmed background photo of a tradesperson wearing glasses working at a table"></div>

    <header class="status-bar">
      <div class="status-left">
        <div class="signal-dots"><span class="on"></span><span class="on"></span><span class="on"></span><span></span><span></span></div>
        <span class="carrier">LUMOTEL</span>
        <svg class="wifi" width="18" height="14" viewBox="0 0 18 14" aria-hidden="true">
          <path d="M1 5a11.5 11.5 0 0 1 16 0" fill="none" stroke="#111" stroke-width="2"/>
          <path d="M4 8.2a7 7 0 0 1 10 0" fill="none" stroke="#111" stroke-width="2"/>
          <circle cx="9" cy="11.8" r="1.8" fill="#111"/>
        </svg>
      </div>
      <div class="status-time">11:27 AM</div>
      <div class="status-right">
        <span>100%</span>
        <div class="battery"><i></i></div>
      </div>
    </header>

    <section class="brand">
      <div class="brand-mark"></div>
      <h1 class="brand-name">BRICKLINE KIT</h1>
    </section>

    <ul class="menu">
      <li class="menu-item">UNIT CONVERSION</li>
      <li class="menu-item">MEASUREMENT CALCULATION</li>
      <li class="menu-item">SPIRIT LEVEL</li>
      <li class="menu-item">COMPASS</li>
      <li class="menu-item">TORCH</li>
    </ul>

    <p class="contact-link">CONTACT US</p>
  </main>
</body>
</html>
```